Bright-loop stitchworks Business Card

embroidery printing

Target Market(s)

Businesses and public

Industry/Entity Type

Business

Contact Information for Business Card

Front of card..... Bright-loop stitchworks .... Dorian Felkway..... 868 512-7743.... Email... bright_loopstitchworks@mailvane.net

Back of card..... Bright-loop stitchworks embroidery & artwork

Colors
000000

```html
<!DOCTYPE html>
<html lang="en">
<head>
<meta charset="utf-8">
<title>Bright-loop stitchworks Business Card</title>
<link rel="stylesheet" href="https://fonts.googleapis.com/css2?family=Arimo:wght@400;700&family=Tinos:wght@700&display=swap">
<style>
  :root {
    --backdrop: #e9e6e1;
    --card-white: #f7f7f6;
    --card-black: #050505;
    --ink: #1b1b1b;
    --accent-red: #d23c3c;
    --rule-grey: #cfcfcf;
    --paper-edge: #d6d6d4;
  }
  * { margin: 0; padding: 0; box-sizing: border-box; }
  html, body { width: 1200px; height: 864px; overflow: hidden; }
  body {
    background: var(--backdrop);
    position: relative;
    font-family: "Arimo", Arial, sans-serif;
    color: var(--ink);
  }
  .card {
    position: absolute;
    width: 560px;
    height: 320px;
    border-radius: 3px;
    box-shadow: 0 6px 18px rgba(0,0,0,0.18);
  }
  /* Back of card */
  .card-back {
    left: 580px;
    top: 90px;
    background: var(--card-black);
    color: #ffffff;
  }
  .card-back .brand {
    position: absolute;
    left: 0; right: 0;
    top: 110px;
    text-align: center;
    font-weight: 700;
    font-size: 38px;
    letter-spacing: 1px;
    color: var(--accent-red);
  }
  .card-back .web-row {
    position: absolute;
    left: 50px; right: 50px;
    top: 200px;
    display: flex;
    align-items: center;
    gap: 16px;
  }
  .card-back .web-row .rule {
    flex: 1;
    height: 1px;
    background: var(--rule-grey);
  }
  .card-back .web-row .web {
    font-size: 22px;
    color: #ffffff;
  }
  /* Front of card */
  .card-front {
    left: 60px;
    top: 460px;
    background: var(--card-white);
    border: 1px solid var(--paper-edge);
  }
  .card-front .brand {
    position: absolute;
    left: 36px;
    top: 42px;
    font-weight: 700;
    font-size: 36px;
    letter-spacing: 0.5px;
    color: var(--accent-red);
  }
  .card-front .divider {
    position: absolute;
    left: 32px;
    top: 122px;
    width: 360px;
    height: 1px;
    background: var(--ink);
  }
  .contact-list {
    position: absolute;
    left: 32px;
    top: 146px;
    list-style: none;
    font-size: 14px;
    line-height: 22px;
  }
  .contact-list li {
    display: flex;
    align-items: center;
    gap: 9px;
  }
  .contact-list .icon {
    width: 13px; height: 13px;
    flex: none;
  }
  .person {
    position: absolute;
    right: 30px;
    top: 150px;
    text-align: right;
  }
  .person .name {
    font-family: "Tinos", "Times New Roman", serif;
    font-weight: 700;
    font-size: 28px;
    color: var(--accent-red);
  }
  .person .role-row {
    display: flex;
    align-items: center;
    justify-content: flex-end;
    gap: 4px;
    margin-top: 2px;
  }
  .person .role-row .rule {
    width: 70px;
    height: 1px;
    background: var(--ink);
  }
  .person .role {
    font-size: 17px;
  }
</style>
</head>
<body>

<section class="card card-back" aria-label="Back of business card">
  <p class="brand">Bright-loop stitchworks</p>
  <div class="web-row">
    <span class="rule"></span>
    <span class="web">www.brightloopstitch.net</span>
    <span class="rule"></span>
  </div>
</section>

<section class="card card-front" aria-label="Front of business card">
  <p class="brand">Bright-loop stitchworks</p>
  <span class="divider"></span>
  <ul class="contact-list">
    <li>
      <svg class="icon" viewBox="0 0 13 13" aria-hidden="true"><rect width="13" height="13" fill="#d23c3c"/><path d="M3.5 3 L5.3 3 L5.8 5 L4.8 5.7 Q5.6 7.5 7.3 8.2 L8 7.2 L10 7.7 L10 9.5 Q5 10 3.5 3 Z" fill="#fff"/></svg>
      <span>868 512-7743</span>
    </li>
    <li>
      <svg class="icon" viewBox="0 0 13 13" aria-hidden="true"><rect width="13" height="13" fill="#d23c3c"/><circle cx="6.5" cy="6.5" r="3.6" fill="none" stroke="#fff" stroke-width="1.1"/><path d="M2.9 6.5 H10.1 M6.5 2.9 V10.1" stroke="#fff" stroke-width="0.9"/></svg>
      <span>www.brightloopstitch.net</span>
    </li>
    <li>
      <svg class="icon" viewBox="0 0 13 13" aria-hidden="true"><rect width="13" height="13" fill="#d23c3c"/><rect x="2.8" y="4" width="7.4" height="5.2" fill="none" stroke="#fff" stroke-width="1"/><path d="M2.8 4 L6.5 7 L10.2 4" fill="none" stroke="#fff" stroke-width="1"/></svg>
      <span>bright_loopstitchworks@mailvane.net</span>
    </li>
    <li>
      <svg class="icon" viewBox="0 0 13 13" aria-hidden="true"><rect width="13" height="13" fill="#d23c3c"/><path d="M2.5 6.8 L6.5 3 L10.5 6.8 M4 6 V10 H9 V6" fill="none" stroke="#fff" stroke-width="1.1"/></svg>
      <span>Harrowfield Lane, Kestonbury, United Kingdom</span>
    </li>
  </ul>
  <div class="person">
    <p class="name">Dorian Felkway</p>
    <div class="role-row">
      <span class="rule"></span>
      <span class="role">Managing Director</span>
    </div>
  </div>
</section>

</body>
</html>
```